Poster

I need a poster for my business, www.coastaltablejourneysbay.example which some information about the most important activities (Sangria Tasting, Iberian Ham, Charcuteries & Sherry Wine Tasting, Sailboat Experiences and Picnic Experiences). A3 Format. Social media included (@coastaltablejourneyctj), contact information included.

```html
<!DOCTYPE html>
<html lang="en">
<head>
<meta charset="utf-8">
<title>Coastal Table Journeys Bay – Poster</title>
<link rel="stylesheet" href="https://fonts.googleapis.com/css2?family=Bebas+Neue&family=Kaushan+Script&family=Montserrat:ital,wght@0,500;1,500&display=swap">
<style>
  :root {
    --orange: #eea024;
    --ink: #2b2b2b;
    --white: #ffffff;
    --sea-deep: #1f3a4d;
    --sea-mid: #3f6478;
    --sunset: #d9a56a;
    --panel: rgba(20, 35, 50, 0.35);
    --page: #e9e9e9;
  }
  * { margin: 0; padding: 0; box-sizing: border-box; }
  html, body { width: 1200px; height: 1200px; overflow: hidden; background: var(--page); }
  .poster {
    position: absolute; left: 197px; top: 30px;
    width: 890px; height: 1260px;
    transform: scale(0.905); transform-origin: top left;
    background: var(--orange); overflow: hidden;
    font-family: "Bebas Neue", "Oswald", sans-serif;
  }
  .hero-photo {
    position: absolute; left: 0; top: 0; width: 890px; height: 632px;
    background: linear-gradient(160deg, var(--sea-deep) 0%, var(--sea-mid) 38%, var(--sunset) 62%, #e8dccb 75%, var(--sea-mid) 100%);
  }
  .hero-panel { position: absolute; left: 62px; top: 0; width: 308px; height: 632px; background: var(--panel); }
  .brand {
    position: absolute; left: 32px; top: 44px; width: 364px; height: 195px;
    background: var(--white); display: flex; align-items: center; gap: 22px; padding-left: 30px;
  }
  .brand-mark { width: 92px; height: 92px; border: 6px solid var(--orange); }
  .brand-name { color: var(--ink); font-size: 44px; line-height: 42px; width: 180px; }
  .brand-tag {
    display: block; margin-top: 8px; background: var(--orange); color: var(--white);
    font-family: "Montserrat", sans-serif; font-weight: 500; font-size: 14px; line-height: 30px;
    text-align: center; letter-spacing: 1px;
  }
  .headline { position: absolute; left: 84px; top: 258px; color: var(--white); font-size: 136px; line-height: 112px; }
  .headline-script {
    position: absolute; left: 116px; top: 450px; color: var(--orange);
    font-family: "Kaushan Script", cursive; font-size: 110px; transform: rotate(-12deg);
  }
  .services { position: absolute; left: 41px; top: 632px; width: 580px; height: 444px; background: var(--white); }
  .service {
    position: absolute; border-left: 2px solid var(--orange); padding-left: 12px;
    color: var(--ink); font-size: 58px; line-height: 52px;
  }
  .photo-strip { position: absolute; left: 621px; top: 558px; width: 224px; }
  .photo-strip div { height: 139px; margin-bottom: 5px; }
  .ph-drinks { background: linear-gradient(135deg, #6b6e73, #c9c2bb); }
  .ph-tapas { background: linear-gradient(135deg, #2c2a27, #8a6a48); }
  .ph-bar { background: linear-gradient(135deg, #3b3d3a, #9a8f6f); }
  .ph-picnic { background: linear-gradient(135deg, #7f9bb0, #d7d5cf); }
  .contact-icon { position: absolute; left: 42px; top: 1099px; width: 74px; height: 74px; border-radius: 50%; background: var(--white); }
  .phone { position: absolute; left: 128px; top: 1094px; color: var(--white); font-size: 86px; line-height: 84px; }
  .website {
    position: absolute; left: 46px; top: 1178px; width: 540px; height: 48px;
    background: var(--ink); color: var(--white); font-size: 37px; line-height: 50px; text-align: center;
  }
  .social { position: absolute; left: 610px; top: 1156px; width: 270px; text-align: center; }
  .social-dot { display: inline-block; width: 36px; height: 36px; border-radius: 50%; background: var(--white); }
  .social-handle { color: var(--white); font-family: "Montserrat", sans-serif; font-style: italic; font-size: 19px; margin-top: 4px; }
</style>
</head>
<body>
  <main class="poster">
    <div class="hero-photo" role="img" aria-label="Couple standing at the bow of a sailboat at sunset on the sea"></div>
    <div class="hero-panel"></div>

    <div class="brand">
      <div class="brand-mark"></div>
      <div class="brand-name">Coastal Table Journeys<span class="brand-tag">BAY</span></div>
    </div>

    <h1 class="headline">Enjoy<br>Your</h1>
    <div class="headline-script">Day</div>

    <section class="services">
      <p class="service" style="left:35px;top:46px;">Sangria<br>Tasting</p>
      <p class="service" style="left:256px;top:46px;">Sailboat<br>Experiences</p>
      <p class="service" style="left:35px;top:173px;">Iberian<br>Ham</p>
      <p class="service" style="left:256px;top:173px;">Picnic<br>Experiences</p>
      <p class="service" style="left:35px;top:301px;">Charcuteries &amp;<br>Sherry Wine Tasting</p>
    </section>

    <div class="photo-strip">
      <div class="ph-drinks" role="img" aria-label="Friends enjoying glasses of sangria"></div>
      <div class="ph-tapas" role="img" aria-label="Olives and tapas served on a table"></div>
      <div class="ph-bar" role="img" aria-label="Chef presenting paella at a wine bar"></div>
      <div class="ph-picnic" role="img" aria-label="Picnic basket with food by the sea"></div>
    </div>

    <div class="contact-icon"></div>
    <p class="phone">+34 600 12 34 56</p>
    <p class="website">WWW.COASTALTABLEJOURNEYSBAY.EXAMPLE</p>

    <div class="social">
      <span class="social-dot"></span>
      <p class="social-handle">@coastaltablejourneyctj</p>
    </div>
  </main>
</body>
</html>
```